Quorvane - corporate Business Card

We need a good look and innovative business card for a new start up company based in Los Angeles called "Quorvane". We are in a payment business, including payment card, app, and ewallet. We are expert in online payment and Card not present (CNP) transaction.
We need an innovative, modern business card.

Our logo font is Aero Matics

Target Market(s)

Startup - Bank - Online Payment - Card Manufacturing

Industry/Entity Type

Startup

Contact Information for Business Card

phone: 424 555 0173 - Address: 4270 Marbrook blvd, Brenmoor City, CA 90871

Requirements
Must have
• Message: innovative, professional, expert, high tech, trust, online payment expert, security
Nice to have
• no comment
Should not have
• no Comment

```html
<!DOCTYPE html>
<html lang="en">
<head>
<meta charset="utf-8">
<title>Quorvane – Business Card</title>
<link rel="stylesheet" href="https://fonts.googleapis.com/css2?family=Arimo:wght@400;700&display=swap">
<style>
  :root {
    --stage: #2b2b2d;
    --brand-red: #b01f2e;
    --brand-red-dark: #8e1623;
    --card-white: #f7f7f7;
    --ink: #1c1c1c;
    --on-red: #ffffff;
  }
  * { box-sizing: border-box; margin: 0; padding: 0; }
  html, body {
    width: 1200px; height: 997px; overflow: hidden;
    background: var(--stage);
    font-family: "Arimo", Arial, sans-serif;
  }
  .card {
    position: absolute;
    width: 560px; height: 320px;
    border-radius: 8px;
    box-shadow: 0 18px 40px rgba(0,0,0,.45);
    overflow: hidden;
  }
  .brand-dot { display: block; border-radius: 50%; }
  .brand-name { font-weight: 700; letter-spacing: 1px; line-height: 1; }

  /* Front */
  .card--front {
    left: 170px; top: 120px;
    background: linear-gradient(160deg, var(--brand-red) 0%, var(--brand-red-dark) 100%);
    display: flex; flex-direction: column; align-items: center; justify-content: center; gap: 16px;
  }
  .card--front .brand-dot { width: 110px; height: 110px; background: var(--on-red); }
  .card--front .brand-name { color: var(--on-red); font-size: 52px; }

  /* Back */
  .card--back {
    left: 470px; top: 520px;
    background: var(--card-white);
  }
  .edge-band {
    position: absolute; top: 40px; width: 14px; height: 240px;
    background: var(--brand-red);
  }
  .edge-band--left { left: 0; border-radius: 0 10px 10px 0; }
  .edge-band--right { right: 0; border-radius: 10px 0 0 10px; }
  .brand-block {
    position: absolute; left: 30px; top: 62px; width: 250px;
    display: flex; flex-direction: column; align-items: center; gap: 16px;
  }
  .card--back .brand-dot { background: var(--brand-red); width: 110px; height: 110px; }
  .card--back .brand-name { color: var(--brand-red); font-size: 44px; }
  .divider {
    position: absolute; left: 288px; top: 40px; width: 2px; height: 240px;
    background: linear-gradient(to bottom, transparent, var(--brand-red) 50%, transparent);
  }
  .contact {
    position: absolute; left: 312px; top: 62px; width: 230px;
    font-size: 14px; line-height: 1.25; color: var(--ink);
  }
  .contact__name { color: var(--brand-red); font-weight: 700; font-size: 16px; }
  .contact__role { font-size: 12px; margin-bottom: 14px; }
  .contact__address { color: var(--brand-red); margin-bottom: 16px; }
  .contact__row { display: flex; align-items: flex-start; gap: 10px; margin-bottom: 8px; }
  .contact__icon { flex: none; width: 20px; height: 20px; }
</style>
</head>
<body>
  <section class="card card--front" aria-label="Card front">
    <span class="brand-dot"></span>
    <span class="brand-name">quorvane</span>
  </section>

  <section class="card card--back" aria-label="Card back">
    <span class="edge-band edge-band--left"></span>
    <span class="edge-band edge-band--right"></span>

    <div class="brand-block">
      <span class="brand-dot"></span>
      <span class="brand-name">quorvane</span>
    </div>

    <span class="divider"></span>

    <div class="contact">
      <p class="contact__name">DELORA VANCE</p>
      <p class="contact__role">Attorney</p>
      <p class="contact__address">4270 Marbrook blvd, Brenmoor City,<br>CA 90871</p>
      <div class="contact__row">
        <svg class="contact__icon" viewBox="0 0 20 20" aria-hidden="true">
          <circle cx="10" cy="10" r="10" fill="var(--brand-red)"/>
          <path d="M5 8c0-2 2-3 5-3s5 1 5 3l-2 1-1-2H8L7 9z M6 10h8l1 4H5z" fill="#fff"/>
        </svg>
        <span>424 555 0173</span>
      </div>
      <div class="contact__row">
        <svg class="contact__icon" viewBox="0 0 20 20" aria-hidden="true">
          <circle cx="10" cy="10" r="10" fill="var(--brand-red)"/>
          <rect x="5" y="6.5" width="10" height="7" fill="#fff"/>
          <path d="M5 6.5l5 4 5-4" fill="none" stroke="var(--brand-red)" stroke-width="1"/>
        </svg>
        <span>4270 Marbrook blvd,<br>Brenmoor City, CA 90871</span>
      </div>
    </div>
  </section>
</body>
</html>
```